Coffeeshop menu for filter tip

We want to have a cannabis (coffeeshop) menu in the size 25mm wide x 60mm wide. Some examples attached.

it must have the following text:
Menu

WEED p/g
Velotrine €16
Cinderfox €14
Tide Rambler €14
Marigolden €16
Grand Pelican €14
Copper Comet €14

HASH p/g
Baltic Ember €12
Harbor Velvet€11
Plum Rova €14
Dusk Maple €10

Target Market(s)

tourist in Amsterdam

Requirements
Nice to have
• cannabis sign leaf
• No Cigarettes allowed symbol

```html
<!DOCTYPE html>
<html lang="en">
<head>
<meta charset="utf-8">
<title>Coffeeshop Menu</title>
<link rel="stylesheet" href="https://fonts.googleapis.com/css2?family=Exo+2:ital,wght@0,700;0,800;1,600&family=Kaushan+Script&display=swap">
<style>
  :root {
    --leaf-dark: #1f3312;
    --leaf-mid: #3f6a1f;
    --leaf-light: #79a63a;
    --panel: rgba(10, 16, 8, 0.86);
    --yellow: #f3e600;
    --green: #17a84a;
    --green-dark: #0d7a33;
    --white: #ffffff;
    --no-red: #e02020;
  }
  * { margin: 0; padding: 0; box-sizing: border-box; }
  html, body { width: 1200px; height: 2880px; overflow: hidden; background: var(--leaf-dark); }
  .menu-canvas { position: relative; width: 1200px; height: 2880px; overflow: hidden; font-family: "Exo 2", sans-serif; }
  .foliage-backdrop {
    position: absolute; inset: 0;
    background:
      radial-gradient(ellipse at 30% 10%, var(--leaf-light) 0%, transparent 45%),
      radial-gradient(ellipse at 80% 55%, var(--leaf-mid) 0%, transparent 50%),
      radial-gradient(ellipse at 20% 85%, var(--leaf-mid) 0%, transparent 45%),
      linear-gradient(180deg, var(--leaf-mid) 0%, var(--leaf-dark) 50%, var(--leaf-mid) 100%);
  }
  .menu-title {
    position: absolute; top: 20px; left: 0; width: 100%; text-align: center;
    font-family: "Kaushan Script", cursive; font-size: 290px; line-height: 1;
    color: var(--white); text-shadow: 0 6px 18px rgba(0,0,0,0.5);
  }
  .section-panel { position: absolute; left: 29px; width: 1142px; background: var(--panel); }
  .section-panel.weed { top: 528px; height: 1212px; }
  .section-panel.hash { top: 1872px; height: 840px; }
  .side-bar { position: absolute; width: 48px; background: var(--yellow); }
  .side-bar.left { left: 0; }
  .side-bar.right { right: 0; width: 53px; }
  .section-heading {
    position: absolute; left: 0; width: 100%; text-align: center;
    font-family: "Kaushan Script", cursive; font-size: 130px; line-height: 1;
    color: var(--yellow);
  }
  .section-unit {
    position: absolute; left: 0; width: 100%; text-align: center;
    font-weight: 700; font-size: 22px; color: var(--yellow);
  }
  .menu-row {
    position: absolute; left: 91px; width: 1037px; height: 96px;
    display: flex; align-items: center;
  }
  .item-name {
    font-weight: 800; font-size: 48px; color: var(--white);
    text-transform: uppercase; white-space: nowrap; padding-right: 14px;
    letter-spacing: 0.5px;
  }
  .leader { flex: 1; height: 3px; background: var(--yellow); }
  .price-tag { flex: none; width: 310px; height: 96px; display: block; }
  .price-tag .currency { font-family: "Exo 2", sans-serif; font-weight: 700; font-size: 34px; fill: var(--white); }
  .price-tag .amount { font-family: "Exo 2", sans-serif; font-weight: 800; font-size: 78px; fill: var(--white); }
  .no-smoking { position: absolute; left: 552px; top: 2730px; width: 96px; height: 96px; }
  .house-rule {
    position: absolute; top: 2826px; left: 0; width: 100%; text-align: center;
    font-style: italic; font-weight: 600; font-size: 38px; color: var(--white);
  }
</style>
</head>
<body>
<div class="menu-canvas">
  <div class="foliage-backdrop" role="img" aria-label="Close-up photograph of green cannabis leaves filling the background"></div>

  <h1 class="menu-title">Menu</h1>

  <!-- Weed section -->
  <div class="side-bar left" style="top:828px;height:576px"></div>
  <div class="side-bar right" style="top:828px;height:576px"></div>
  <section class="section-panel weed"></section>
  <div class="section-heading" style="top:455px">Weed</div>
  <div class="section-unit" style="top:585px">p/g</div>

  <div class="menu-row" style="top:662px"><span class="item-name">Velotrine</span><span class="leader"></span>
    <svg class="price-tag" viewBox="0 0 310 96"><polyline points="0,48 22,48 42,90 310,90" fill="none" stroke="#f3e600" stroke-width="3"/><polygon points="24,8 310,8 292,80 42,80" fill="#17a84a"/><polygon points="24,8 310,8 306,22 30,22" fill="#0d7a33" opacity="0.35"/><text class="currency" x="58" y="46">€</text><text class="amount" x="92" y="74">16</text></svg></div>
  <div class="menu-row" style="top:833px"><span class="item-name">Cinderfox</span><span class="leader"></span>
    <svg class="price-tag" viewBox="0 0 310 96"><polyline points="0,48 22,48 42,90 310,90" fill="none" stroke="#f3e600" stroke-width="3"/><polygon points="24,8 310,8 292,80 42,80" fill="#17a84a"/><polygon points="24,8 310,8 306,22 30,22" fill="#0d7a33" opacity="0.35"/><text class="currency" x="58" y="46">€</text><text class="amount" x="92" y="74">14</text></svg></div>
  <div class="menu-row" style="top:1003px"><span class="item-name">Tide Rambler</span><span class="leader"></span>
    <svg class="price-tag" viewBox="0 0 310 96"><polyline points="0,48 22,48 42,90 310,90" fill="none" stroke="#f3e600" stroke-width="3"/><polygon points="24,8 310,8 292,80 42,80" fill="#17a84a"/><polygon points="24,8 310,8 306,22 30,22" fill="#0d7a33" opacity="0.35"/><text class="currency" x="58" y="46">€</text><text class="amount" x="92" y="74">14</text></svg></div>
  <div class="menu-row" style="top:1176px"><span class="item-name">Marigolden</span><span class="leader"></span>
    <svg class="price-tag" viewBox="0 0 310 96"><polyline points="0,48 22,48 42,90 310,90" fill="none" stroke="#f3e600" stroke-width="3"/><polygon points="24,8 310,8 292,80 42,80" fill="#17a84a"/><polygon points="24,8 310,8 306,22 30,22" fill="#0d7a33" opacity="0.35"/><text class="currency" x="58" y="46">€</text><text class="amount" x="92" y="74">16</text></svg></div>
  <div class="menu-row" style="top:1346px"><span class="item-name">Grand Pelican</span><span class="leader"></span>
    <svg class="price-tag" viewBox="0 0 310 96"><polyline points="0,48 22,48 42,90 310,90" fill="none" stroke="#f3e600" stroke-width="3"/><polygon points="24,8 310,8 292,80 42,80" fill="#17a84a"/><polygon points="24,8 310,8 306,22 30,22" fill="#0d7a33" opacity="0.35"/><text class="currency" x="58" y="46">€</text><text class="amount" x="92" y="74">14</text></svg></div>
  <div class="menu-row" style="top:1519px"><span class="item-name">Copper Comet</span><span class="leader"></span>
    <svg class="price-tag" viewBox="0 0 310 96"><polyline points="0,48 22,48 42,90 310,90" fill="none" stroke="#f3e600" stroke-width="3"/><polygon points="24,8 310,8 292,80 42,80" fill="#17a84a"/><polygon points="24,8 310,8 306,22 30,22" fill="#0d7a33" opacity="0.35"/><text class="currency" x="58" y="46">€</text><text class="amount" x="92" y="74">14</text></svg></div>

  <!-- Hash section -->
  <div class="side-bar left" style="top:2172px;height:312px"></div>
  <div class="side-bar right" style="top:2172px;height:312px"></div>
  <section class="section-panel hash"></section>
  <div class="section-heading" style="top:1780px">Hash</div>
  <div class="section-unit" style="top:1910px">p/g</div>

  <div class="menu-row" style="top:2004px"><span class="item-name">Baltic Ember</span><span class="leader"></span>
    <svg class="price-tag" viewBox="0 0 310 96"><polyline points="0,48 22,48 42,90 310,90" fill="none" stroke="#f3e600" stroke-width="3"/><polygon points="24,8 310,8 292,80 42,80" fill="#17a84a"/><polygon points="24,8 310,8 306,22 30,22" fill="#0d7a33" opacity="0.35"/><text class="currency" x="58" y="46">€</text><text class="amount" x="92" y="74">12</text></svg></div>
  <div class="menu-row" style="top:2177px"><span class="item-name">Harbor Velvet</span><span class="leader"></span>
    <svg class="price-tag" viewBox="0 0 310 96"><polyline points="0,48 22,48 42,90 310,90" fill="none" stroke="#f3e600" stroke-width="3"/><polygon points="24,8 310,8 292,80 42,80" fill="#17a84a"/><polygon points="24,8 310,8 306,22 30,22" fill="#0d7a33" opacity="0.35"/><text class="currency" x="58" y="46">€</text><text class="amount" x="92" y="74">11</text></svg></div>
  <div class="menu-row" style="top:2347px"><span class="item-name">Plum Rova</span><span class="leader"></span>
    <svg class="price-tag" viewBox="0 0 310 96"><polyline points="0,48 22,48 42,90 310,90" fill="none" stroke="#f3e600" stroke-width="3"/><polygon points="24,8 310,8 292,80 42,80" fill="#17a84a"/><polygon points="24,8 310,8 306,22 30,22" fill="#0d7a33" opacity="0.35"/><text class="currency" x="58" y="46">€</text><text class="amount" x="92" y="74">14</text></svg></div>
  <div class="menu-row" style="top:2520px"><span class="item-name">Dusk Maple</span><span class="leader"></span>
    <svg class="price-tag" viewBox="0 0 310 96"><polyline points="0,48 22,48 42,90 310,90" fill="none" stroke="#f3e600" stroke-width="3"/><polygon points="24,8 310,8 292,80 42,80" fill="#17a84a"/><polygon points="24,8 310,8 306,22 30,22" fill="#0d7a33" opacity="0.35"/><text class="currency" x="58" y="46">€</text><text class="amount" x="92" y="74">10</text></svg></div>

  <svg class="no-smoking" viewBox="0 0 96 96" role="img" aria-label="No smoking">
    <circle cx="48" cy="48" r="46" fill="#000"/>
    <rect x="18" y="50" width="52" height="11" fill="#fff"/>
    <rect x="72" y="50" width="6" height="11" fill="#fff"/>
    <path d="M66 46 q-4 -8 2 -14 q6 -6 0 -14" fill="none" stroke="#fff" stroke-width="3"/>
    <circle cx="48" cy="48" r="40" fill="none" stroke="#e02020" stroke-width="9"/>
    <line x1="20" y1="20" x2="76" y2="76" stroke="#e02020" stroke-width="9"/>
  </svg>
  <p class="house-rule">No cigarettes allowed.</p>
</div>
</body>
</html>
```